FUN WEBSITE NEEDED FOR NEW ACCESSORY PRINTING COMPANY

NOTE: This is Website Design Only - No coding required

PLEASE SUBMIT YOUR DESIGNS RIGHT AWAY AS WE WANT TO PICK A WINNER ASAP!

Hi,

We are looking for a vibrant and hip website for a new emerging industry that allows us to personalize cell phone covers and many other items with our unique printing ability.

Our site must be hip and vibrant, as our audience is high schoolers and teens for the most part.

The site should be simple and straight forward while at the same time be of high visual quality.

This will be an e-commerce site that will sell around 10 products.

Please provide designs for a great looking site to help us sell our products.

You will find our logo attached. Here is a link to our catalogue so you can get an idea of what we do. Again Cell Phone Covers will be our main priority so please focus on that.

https://www.filevault-example.net/s/qetumaxlor7261/SnapGlo%20Catalog%2011x17.pdf

Thanks!
Todd

Target Market(s)

The target market is high schoolers and teens.

Additional target market is Collage kids

Sports Teams

Industry/Entity Type

Cell Phone

Font styles to use
Sans Serif

Requirements
Must have
• Clean look
Ecommerce
Horizontal menu
Showing cell phone printing from catalogue
Follow Logo Colors
Should not have
• Cluttery design
Hard to read see
Not clean

```html
<!DOCTYPE html>
<html lang="en">
<head>
<meta charset="utf-8">
<title>SnapGlo – Unlimited Personalized Products</title>
<link rel="stylesheet" href="https://fonts.googleapis.com/css2?family=Open+Sans:wght@400;600;700;800&family=Arimo:wght@400;700&display=swap">
<style>
:root{
  --green:#0ccf0c;
  --pink:#f2005e;
  --pink-dark:#d4004f;
  --blue:#1f7ed6;
  --ink:#333;
  --bar:#3a3a3a;
  --cat:#c4c4c4;
  --line:#d8d8d8;
  --footer:#4a4a4a;
  --footer-base:#3b3b3b;
  --navy:#2a2f5a;
}
*{box-sizing:border-box;margin:0;padding:0}
html,body{width:1029px;height:1200px;overflow:hidden;background:#fff}
body{font-family:"Arimo",Arial,sans-serif;color:var(--ink)}
.page{position:relative;width:1200px;height:1400px;transform:scale(.8575);transform-origin:0 0}
.abs{position:absolute}

/* header */
.top-stripe{left:0;top:0;width:1200px;height:7px;background:var(--green)}
.account-bar{left:610px;top:6px;width:490px;height:29px;background:var(--green);clip-path:polygon(0 100%,12px 0,100% 0,488px 0,478px 100%)}
.account-bar a{position:absolute;top:6px;font:700 11px "Open Sans",sans-serif;color:#fff;text-decoration:none}
.account-bar .sep{position:absolute;top:2px;width:1px;height:22px;background:rgba(255,255,255,.6)}
.search{left:917px;top:8px;width:160px;height:18px;background:#fff}
.search svg{position:absolute;right:4px;top:0}
.logo{left:97px;top:42px;display:flex;align-items:center;gap:10px}
.logo .dot{width:30px;height:30px;border-radius:50%;background:var(--pink)}
.logo .name{font:800 38px "Open Sans",sans-serif;color:var(--pink)}
.main-nav{left:365px;top:92px;height:20px}
.main-nav a{position:absolute;top:0;white-space:nowrap;font:400 13px "Open Sans",sans-serif;letter-spacing:-.2px;color:#222;text-decoration:none;line-height:20px}
.main-nav a.active{background:var(--pink);color:#fff;border-radius:4px;padding:0 7px;font-weight:600;letter-spacing:0}
.header-rule{left:0;top:119px;width:1200px;height:4px;background:#eee}

/* hero */
.hero{left:0;top:128px;width:1200px;height:384px;background:linear-gradient(90deg,#ececec 0%,#cfd3d7 30%,#a9b4bf 48%,#c7b3a6 65%,#e9e6e4 100%)}
.phones{position:absolute;left:205px;top:115px;width:470px;height:250px}
.phone{position:absolute;border-radius:14px;box-shadow:0 4px 10px rgba(0,0,0,.25)}
.phone.p1{left:3px;top:4px;width:86px;height:234px;background:linear-gradient(#f4f4f4,#5a9fd8 20%,#3b6fa8 75%,#f0f0f0 92%)}
.phone.p2{left:82px;top:18px;width:104px;height:218px;background:linear-gradient(#1b1b1b 8%,#d8282e 20%,#b81f25 80%,#1b1b1b 92%)}
.phone.p5{left:365px;top:4px;width:98px;height:238px;background:linear-gradient(#1a1a1a 8%,#b97a50 30%,#2b3550 75%,#1a1a1a 92%)}
.phone.p4{left:265px;top:3px;width:112px;height:237px;background:linear-gradient(#e8e8e8 8%,#7ab4e8 28%,#5aa84a 70%,#e4e4e4 92%)}
.phone.p3{left:175px;top:10px;width:120px;height:238px;background:linear-gradient(#141414 10%,#6a6e72 28%,#3a6fa8 65%,#141414 88%)}
.hero-title{left:732px;top:153px;font:800 38px/36px "Open Sans",sans-serif;color:var(--pink)}
.hero-sub{left:731px;top:232px;font:400 16px/22px "Open Sans",sans-serif;color:#555}
.hero-btn{left:735px;top:305px;width:132px;height:41px;border-radius:5px;background:linear-gradient(#ff2a7a,var(--pink-dark));color:#fff;font:700 24px/41px "Open Sans",sans-serif;text-align:center}

/* panels */
.panel{border:1px solid var(--line);background:#fff}
.panel-head{position:absolute;left:0;top:0;right:0;height:43px;background:linear-gradient(#ff1a6e,var(--pink-dark));color:#fff;font:400 18px/43px "Arimo",sans-serif;padding-left:16px;letter-spacing:.3px}
.featured{left:100px;top:552px;width:662px;height:426px}
.product{position:absolute;width:188px}
.product .shot{position:relative;height:114px;border:1px solid #ccc;background:#fff;overflow:hidden}
.shot i{position:absolute;display:block}
.product .buy{margin-top:8px;height:35px;background:var(--bar);color:#fff;font:400 14px/35px "Arimo",sans-serif;display:flex;justify-content:space-between;padding:0 28px 0 25px}
.categories{left:824px;top:552px;width:276px;height:202px}
.cat-list{position:absolute;left:8px;top:49px;width:259px;list-style:none}
.cat-list li{height:25px;margin-bottom:5px;background:var(--cat);font:400 14px/25px "Arimo",sans-serif;color:#444;padding-left:13px;position:relative}
.cat-list li .arr{position:absolute;right:8px;top:0;font-size:16px}
.promo{left:824px;top:765px;width:275px;height:225px;border:1px solid #e2e2e2;background:#fff;overflow:hidden}
.promo .t1{position:absolute;left:4px;top:4px;font:700 27px "Open Sans",sans-serif;color:var(--pink)}
.promo .t2{position:absolute;left:147px;top:16px;font:700 27px "Open Sans",sans-serif;color:var(--navy)}
.promo .t3{position:absolute;left:8px;top:54px;font:400 13px "Open Sans",sans-serif;color:#5a2b3b}
.promo .tag{position:absolute;left:5px;top:82px;width:186px;height:25px;background:var(--pink);border-radius:3px;color:#fff;font:600 12px/25px "Open Sans",sans-serif;padding-left:22px}
.promo .price{position:absolute;left:22px;top:104px;font:800 32px "Open Sans",sans-serif;color:#fff;background:#8a0f52;padding:0 6px;border-radius:4px}
.promo .people{position:absolute;left:100px;top:88px;width:175px;height:137px;background:linear-gradient(120deg,#fff 10%,#c99a7a 35%,#6b4532 55%,#2aa6d8 85%)}
.promo .small{position:absolute;left:9px;top:196px;font:700 8px/10px "Open Sans",sans-serif;color:#333}

/* feature cards */
.card{top:1022px;width:324px;height:115px;border:1px solid #d0d0d0;background:linear-gradient(#fff 55%,#e8e8e8)}
.card h3{position:absolute;left:26px;top:20px;font:400 20px "Arimo",sans-serif}
.card p{position:absolute;left:28px;top:54px;font:400 12px "Arimo",sans-serif;color:#333}
.card .btn{position:absolute;left:29px;top:82px;width:96px;height:24px;border-radius:3px;background:linear-gradient(#ff2a7a,var(--pink-dark));color:#fff;font:700 12px/24px "Arimo",sans-serif;text-align:center}

/* footer */
.footer-rule{left:0;top:1185px;width:1200px;height:7px;background:var(--pink)}
.footer{left:0;top:1192px;width:1200px;height:170px;background:var(--footer)}
.footer-base{left:0;top:1362px;width:1200px;height:38px;background:var(--footer-base)}
.foot-col{position:absolute;top:44px;list-style:none}
.foot-col li{height:20px;font:400 12px "Arimo",sans-serif;letter-spacing:.6px;color:#fff;padding-left:25px;position:relative}
.foot-col li::before{content:"»";position:absolute;left:0;top:-2px;color:var(--pink);font-size:15px}
.copyright{left:0;top:1347px;width:1200px;text-align:center;font:400 12px "Arimo",sans-serif;letter-spacing:.5px;color:#fff}
</style>
</head>
<body>
<div class="page">

  <div class="abs top-stripe"></div>
  <nav class="abs account-bar">
    <a style="left:24px">View My Account</a><span class="sep" style="left:122px"></span>
    <a style="left:139px">View My Cart</a><span class="sep" style="left:216px"></span>
    <a style="left:235px">Check out</a>
  </nav>
  <div class="abs search">
    <svg width="24" height="18" viewBox="0 0 24 18"><circle cx="9" cy="7" r="5.5" fill="none" stroke="#111" stroke-width="2.2"/><line x1="13" y1="11" x2="20" y2="17" stroke="#111" stroke-width="3"/></svg>
  </div>

  <div class="abs logo"><span class="dot"></span><span class="name">SnapGlo</span></div>

  <nav class="abs main-nav">
    <a class="active" style="left:0">Home</a>
    <a style="left:75px">Product Range</a>
    <a style="left:180px">Custom Promotional Products</a>
    <a style="left:376px">Company</a>
    <a style="left:461px">Artwork</a>
    <a style="left:538px">Custom Made Express</a>
    <a style="left:688px">Contact</a>
  </nav>
  <div class="abs header-rule"></div>

  <section class="abs hero">
    <div class="phones" role="img" aria-label="Row of five smartphones with custom printed covers and colourful screens">
      <span class="phone p1" aria-hidden="true"></span>
      <span class="phone p2" aria-hidden="true"></span>
      <span class="phone p5" aria-hidden="true"></span>
      <span class="phone p4" aria-hidden="true"></span>
      <span class="phone p3" aria-hidden="true"></span>
    </div>
    <h1 class="abs hero-title">SPECIAL<br>OFFER</h1>
    <p class="abs hero-sub">IRURE DOLOR IN REPREHENDERIT<br>IN VOLUPTATE</p>
    <div class="abs hero-btn">Read More</div>
  </section>

  <section class="abs panel featured">
    <h2 class="panel-head">FEATURED PRODUCTS</h2>
    <div class="product" style="left:24px;top:66px"><div class="shot" role="img" aria-label="Red, pink and blue printed phone covers">
      <i style="left:28px;top:6px;width:42px;height:92px;border-radius:9px;background:#e8262c"></i>
      <i style="left:68px;top:12px;width:44px;height:90px;border-radius:9px;background:#e0409e"></i>
      <i style="left:104px;top:10px;width:48px;height:98px;border-radius:10px;background:#2fa8e2"></i>
    </div><div class="buy"><span>BUY</span><span>$899</span></div></div>
    <div class="product" style="left:236px;top:66px"><div class="shot" role="img" aria-label="Yellow t-shirt with a printed city design">
      <i style="left:42px;top:6px;width:104px;height:104px;border-radius:18px 18px 4px 4px;background:#e8ff1a"></i>
    </div><div class="buy"><span>BUY</span><span>$899</span></div></div>
    <div class="product" style="left:447px;top:66px"><div class="shot" role="img" aria-label="Pair of pink strappy high heels">
      <i style="left:40px;top:8px;width:110px;height:96px;border-radius:40px 40px 10px 10px;background:#ff5f97"></i>
    </div><div class="buy"><span>BUY</span><span>$899</span></div></div>
    <div class="product" style="left:25px;top:235px"><div class="shot" role="img" aria-label="Printed door hanger tags">
      <i style="left:36px;top:6px;width:96px;height:100px;border-radius:30px 30px 6px 6px;background:#c6b4d6"></i>
    </div><div class="buy"><span>BUY</span><span>$899</span></div></div>
    <div class="product" style="left:235px;top:235px"><div class="shot" role="img" aria-label="Soccer ball and American football">
      <i style="left:14px;top:12px;width:92px;height:92px;border-radius:50%;background:#3d4f9e"></i>
      <i style="left:106px;top:30px;width:74px;height:70px;border-radius:50%;background:#7e3526"></i>
    </div><div class="buy"><span>BUY</span><span>$899</span></div></div>
    <div class="product" style="left:447px;top:235px"><div class="shot" role="img" aria-label="Two red baseball caps">
      <i style="left:16px;top:8px;width:82px;height:60px;border-radius:40px 40px 10px 10px;background:#d81e2a"></i>
      <i style="left:70px;top:22px;width:104px;height:82px;border-radius:50px 50px 14px 14px;background:#c8141f"></i>
    </div><div class="buy"><span>BUY</span><span>$899</span></div></div>
  </section>

  <aside class="abs panel categories">
    <h2 class="panel-head">CATEGORIES</h2>
    <ul class="cat-list">
      <li>ACCESSORIES<span class="arr">»</span></li>
      <li>CPUS</li>
      <li>HARD DRIVES</li>
      <li>KEYBOARDS &amp; MICE</li>
      <li>MONITORS</li>
    </ul>
  </aside>

  <aside class="abs promo">
    <span class="t1">Clothing &amp;</span>
    <span class="t2">Apparel</span>
    <span class="t3">GET A BANNER FOR YOUR BUSINESS</span>
    <div class="people" role="img" aria-label="Two smiling people promoting apparel"></div>
    <span class="tag">PRICES STARTING AT</span>
    <span class="price">$30</span>
    <span class="small">METRO PULSE<br>WEB SERVICES</span>
  </aside>

  <article class="abs card" style="left:100px">
    <h3 style="color:var(--blue)">NOVA PHONE S3</h3>
    <p>Ipsum has been the industry's standard</p>
    <span class="btn">Read More</span>
  </article>
  <article class="abs card" style="left:439px">
    <h3 style="color:var(--pink)">LUMEN TILE 610</h3>
    <p>Ipsum has been the industry's standard</p>
    <span class="btn">Read More</span>
  </article>
  <article class="abs card" style="left:777px">
    <h3 style="color:var(--green)">KESTREL ASPIRE</h3>
    <p>Ipsum has been the industry's standard</p>
    <span class="btn">Read More</span>
  </article>

  <div class="abs footer-rule"></div>
  <footer class="abs footer">
    <ul class="foot-col" style="left:142px"><li>Powered Speakers Budget</li><li>Power Amplifiers</li><li>Active Speakers</li><li>Passive Speakers</li><li>Split Systems</li></ul>
    <ul class="foot-col" style="left:349px;top:43px"><li>Hardware</li><li>DJ Gear Spare Parts</li><li>Drivers / Tweeters / X-Overs</li><li>Power Supplies</li><li>Electronics</li></ul>
    <ul class="foot-col" style="left:568px;top:45px"><li>Home Audio</li><li>DJ Packages</li><li>Speaker Packs</li><li>Lighting Packs</li><li>PA Packages</li></ul>
    <ul class="foot-col" style="left:741px;top:46px"><li>Clamps</li><li>Lighting Stands</li><li>DJ Stands</li><li>Speaker Stands</li><li>Music Stands</li></ul>
    <ul class="foot-col" style="left:945px;top:45px"><li>Home Audio</li><li>DJ Packages</li><li>Speaker Packs</li><li>Lighting Packs</li><li>PA Packages</li></ul>
  </footer>
  <div class="abs footer-base"></div>
  <p class="abs copyright">© 2012 SnapGlo&nbsp; Unlimited personalized products&nbsp; Essentials.</p>

</div>
</body>
</html>
```